Company PowerPoint Presentation Template

I am looking for a business powerpoint template tailored to my company that specializes in permafrost services for the mining, transportation, and oil & gas industries. The template would be used to present project findings from studies completed for our clients. I am looking for a crisp, technical, professional business look to the template. Our business is located in North America and English is the primary language used to communicate our work. Complimentary colors associated with the business is blue (RGB, 0,112,192) or something similar in color.

```html
<!DOCTYPE html>
<html lang="en">
<head>
<meta charset="utf-8">
<title>Tundraline Permafrost Consulting – Presentation Template</title>
<link href="https://fonts.googleapis.com/css2?family=Montserrat:wght@500;600;700;800&family=Open+Sans:wght@400;600&display=swap" rel="stylesheet">
<style>
:root{
  --blue:#0070c0;
  --blue-dark:#0a4f8f;
  --navy:#0b2a4a;
  --ice:#9fc7e6;
  --ice-light:#d8e8f4;
  --page:#e8ebee;
  --text:#3c4650;
  --muted:#8a96a3;
  --white:#ffffff;
}
*{box-sizing:border-box;margin:0;padding:0}
html,body{width:1200px;height:2164px;overflow:hidden}
body{background:var(--page);font-family:"Open Sans",Arial,sans-serif;color:var(--text);position:relative}
.hero{position:absolute;left:150px;top:60px;width:900px;height:507px;box-shadow:0 10px 30px rgba(0,0,0,.18)}
.hero .slide{transform:scale(1.6791);transform-origin:0 0;box-shadow:none}
.deck{position:absolute;left:48px;top:650px;display:grid;grid-template-columns:536px 536px;column-gap:32px;row-gap:56px}
.slide{position:relative;width:536px;height:302px;background:var(--white);overflow:hidden;box-shadow:0 4px 14px rgba(0,0,0,.12)}
.logo{font-family:"Montserrat",Arial,sans-serif;font-weight:800;color:var(--navy);letter-spacing:2px;font-size:17px;display:flex;align-items:center;gap:6px;text-transform:uppercase}
.logo .mark{width:9px;height:9px;background:var(--navy)}
.logo.small{font-size:10px;letter-spacing:1.2px}
.logo.small .mark{width:6px;height:6px}
.logo.light{color:var(--white)}
.logo.light .mark{background:var(--white)}
.photo{position:absolute}
/* title slide */
.title-head{position:absolute;left:24px;top:16px}
.date-tag{position:absolute;right:22px;top:18px;background:var(--blue);color:var(--white);font-size:6px;padding:4px 10px;border-radius:2px}
.title-band{position:absolute;left:0;top:50px;width:536px;height:168px;background:linear-gradient(90deg,var(--blue-dark),var(--blue))}
.title-band .photo{right:0;top:0;width:330px;height:168px;background:linear-gradient(120deg,#5d9bd0 0%,#a9cbe6 45%,#dfeaf3 75%,#7ea9cf 100%);clip-path:polygon(18% 0,100% 0,100% 100%,0 100%);opacity:.9}
.title-band .shade{position:absolute;left:180px;top:0;width:200px;height:168px;background:linear-gradient(90deg,var(--blue) 0%,rgba(0,112,192,0) 100%)}
.title-text{position:absolute;left:24px;top:52px;z-index:2}
.title-text h1{font-family:"Montserrat",Arial,sans-serif;font-weight:700;color:var(--white);font-size:27px;line-height:1.08}
.title-text p{font-family:"Montserrat",Arial,sans-serif;color:var(--ice-light);font-size:10px;margin-top:5px;font-weight:500}
.title-foot{position:absolute;left:24px;bottom:22px;font-size:5px;color:var(--muted);line-height:1.5}
.title-foot b{color:var(--navy)}
/* content slides */
.banner{position:absolute;left:0;top:0;width:536px;height:70px;background:linear-gradient(90deg,var(--blue-dark),var(--blue) 60%,#4d95cf)}
.banner h2{font-family:"Montserrat",Arial,sans-serif;font-weight:700;color:var(--white);font-size:15px;position:absolute;width:100%;text-align:center;top:26px}
.foot{position:absolute;left:20px;right:20px;bottom:12px;display:flex;align-items:center;justify-content:space-between}
.foot small{font-size:4.5px;color:var(--muted)}
.pg{width:12px;height:12px;border-radius:50%;background:var(--blue);color:var(--white);font-size:6px;display:flex;align-items:center;justify-content:center;font-weight:600}
.pillars{position:absolute;top:46px;left:40px;right:40px;display:flex;justify-content:space-between}
.pillar{width:128px;text-align:center}
.pillar .icon{width:46px;height:46px;margin:0 auto;border-radius:50%;background:var(--white);border:2px solid var(--blue);display:flex;align-items:center;justify-content:center}
.pillar h3{font-family:"Montserrat",Arial,sans-serif;font-size:8px;color:var(--navy);margin-top:10px;font-weight:700}
.pillar p{font-size:5px;line-height:1.55;margin-top:5px;color:var(--text)}
/* bio */
.bio-name{position:absolute;left:28px;top:40px}
.bio-name h2{font-family:"Montserrat",Arial,sans-serif;font-weight:700;color:var(--navy);font-size:19px;line-height:1.1}
.bio-name p{font-size:7px;color:var(--blue);margin-top:6px;font-weight:600}
.bio-photo{right:0;top:0;width:250px;height:302px;background:linear-gradient(160deg,#8fb5d6,#3f7fb8 55%,#1d5a92)}
.bio-band{position:absolute;left:0;top:150px;width:286px;height:152px;background:var(--blue);padding:18px 24px}
.bio-band p{font-size:5.2px;line-height:1.6;color:var(--ice-light);margin-bottom:6px}
/* services */
.services{position:absolute;top:46px;left:28px;right:28px;display:flex;justify-content:space-between}
.svc{width:148px;text-align:center}
.svc .photo{position:relative;width:148px;height:98px;border:3px solid var(--white);box-shadow:0 2px 6px rgba(0,0,0,.15)}
.svc h3{font-family:"Montserrat",Arial,sans-serif;font-size:7px;color:var(--navy);font-weight:700;margin-top:9px;line-height:1.3}
.svc p{font-size:4.6px;line-height:1.5;margin-top:4px;color:var(--text)}
.g1{background:linear-gradient(160deg,#9fb7c9,#5f7f99)}
.g2{background:linear-gradient(160deg,#c8d6e2,#7b8c9a)}
.g3{background:linear-gradient(160deg,#e6edf3,#a4b8c8)}
.g4{background:linear-gradient(160deg,#d8c46a,#6f7a4a)}
.g5{background:linear-gradient(160deg,#b9a98a,#4f6b7e)}
.g6{background:linear-gradient(160deg,#c7d7e4,#8aa3b7)}
.g7{background:linear-gradient(160deg,#a8a8a0,#5e5f5a)}
.g8{background:linear-gradient(160deg,#7d7f86,#2f3238)}
.g9{background:linear-gradient(160deg,#e7e0d4,#a59a88)}
/* contact */
.contact-logo{position:absolute;left:0;right:0;top:92px;display:flex;justify-content:center}
.contact-logo .logo{font-size:22px}
.contact-band{position:absolute;left:0;bottom:0;width:536px;height:120px;background:linear-gradient(90deg,var(--blue-dark),var(--blue))}
.contact-band h2{font-family:"Montserrat",Arial,sans-serif;font-weight:700;color:var(--white);font-size:12px;position:absolute;left:40px;top:20px}
.contact-list{position:absolute;left:40px;top:44px;list-style:none}
.contact-list li{display:flex;align-items:center;gap:7px;color:var(--white);font-size:6.5px;margin-bottom:6px}
.contact-list svg{width:9px;height:9px}
</style>
</head>
<body>

<div class="hero">
  <section class="slide title-slide">
    <div class="title-head"><div class="logo"><span class="mark"></span>Tundraline</div></div>
    <div class="date-tag">Monday, June 5, 2023</div>
    <div class="title-band">
      <div class="photo" role="img" aria-label="Photo of frozen arctic ground and ice under a clear sky"></div>
      <div class="shade"></div>
      <div class="title-text">
        <h1>Expert<br>Permafrost Services</h1>
        <p>Innovative Solutions to Meet Cold Region Challenges</p>
      </div>
    </div>
    <div class="title-foot"><b>Confidential</b> © 2023 Tundraline Permafrost Consulting Ltd.<br>All rights reserved. Not for distribution.</div>
  </section>
</div>

<div class="deck">

  <section class="slide title-slide">
    <div class="title-head"><div class="logo"><span class="mark"></span>Tundraline</div></div>
    <div class="date-tag">Monday, June 5, 2023</div>
    <div class="title-band">
      <div class="photo" role="img" aria-label="Photo of frozen arctic ground and ice under a clear sky"></div>
      <div class="shade"></div>
      <div class="title-text">
        <h1>Expert<br>Permafrost Services</h1>
        <p>Innovative Solutions to Meet Cold Region Challenges</p>
      </div>
    </div>
    <div class="title-foot"><b>Confidential</b> © 2023 Tundraline Permafrost Consulting Ltd.<br>All rights reserved. Not for distribution.</div>
  </section>

  <section class="slide title-slide">
    <div class="title-head"><div class="logo"><span class="mark"></span>Tundraline</div></div>
    <div class="date-tag">Monday, June 5, 2023</div>
    <div class="title-band">
      <div class="photo" role="img" aria-label="Photo of snow covered permafrost terrain"></div>
      <div class="shade"></div>
      <div class="title-text">
        <h1>Presentation<br>Title Goes Here</h1>
        <p>Sub Title of Presentation Goes Here</p>
      </div>
    </div>
    <div class="title-foot"><b>Confidential</b> © 2023 Tundraline Permafrost Consulting Ltd.<br>All rights reserved. Not for distribution.</div>
  </section>

  <section class="slide about-slide">
    <div class="banner"><h2>About Us</h2></div>
    <div class="pillars" style="top:50px">
      <div class="pillar">
        <div class="icon"><svg width="20" height="20" viewBox="0 0 24 24" fill="none" stroke="#0070c0" stroke-width="2"><circle cx="12" cy="12" r="9"/><circle cx="12" cy="12" r="5"/><circle cx="12" cy="12" r="1.5" fill="#0070c0"/></svg></div>
        <h3>Our Mission</h3>
        <p>We deliver reliable permafrost science and engineering that keeps northern projects safe, efficient and sustainable.</p>
      </div>
      <div class="pillar">
        <div class="icon"><svg width="20" height="20" viewBox="0 0 24 24" fill="none" stroke="#0070c0" stroke-width="2"><path d="M2 12s4-7 10-7 10 7 10 7-4 7-10 7S2 12 2 12z"/><circle cx="12" cy="12" r="3"/></svg></div>
        <h3>Our Vision</h3>
        <p>To be the trusted partner for cold region development across mining, transport and energy sectors.</p>
      </div>
      <div class="pillar">
        <div class="icon"><svg width="20" height="20" viewBox="0 0 24 24" fill="none" stroke="#0070c0" stroke-width="2"><circle cx="12" cy="12" r="3"/><path d="M12 2v4M12 18v4M2 12h4M18 12h4M5 5l3 3M16 16l3 3M5 19l3-3M16 8l3-3"/></svg></div>
        <h3>Our Services</h3>
        <p>Site investigation, thermal design, modelling, monitoring and hazard mapping for frozen ground.</p>
      </div>
    </div>
    <div class="foot"><div class="logo small"><span class="mark"></span>Tundraline</div><small>Tundraline Permafrost Consulting Ltd. | Confidential</small><div class="pg">3</div></div>
  </section>

  <section class="slide bio-slide">
    <div class="bio-name"><h2>Daniel<br>Harrow, PhD</h2><p>Principal Consultant</p></div>
    <div class="photo bio-photo" role="img" aria-label="Portrait photo of the principal consultant"></div>
    <div class="bio-band">
      <p>Daniel is a geotechnical engineer with over twenty years of experience on permafrost projects across northern Canada and Alaska.</p>
      <p>He leads thermal design and ground investigation work for mines, highways and pipelines, and advises clients on climate resilient infrastructure.</p>
      <p>He holds a doctorate in cold regions engineering.</p>
    </div>
  </section>

  <section class="slide services-slide">
    <div class="banner"><h2 style="left:0">Core Services</h2></div>
    <div class="services">
      <div class="svc"><div class="photo g1" role="img" aria-label="Photo of a drill rig collecting frozen ground cores"></div><h3>Permafrost and Ground Ice Investigation</h3><p>Drilling, sampling and testing of frozen soils.</p></div>
      <div class="svc"><div class="photo g2" role="img" aria-label="Photo of a road built over frozen terrain"></div><h3>Thermal Design of Infrastructure</h3><p>Foundations and embankments for cold ground.</p></div>
      <div class="svc"><div class="photo g3" role="img" aria-label="Photo of a snowy landscape under study"></div><h3>Thermal Modelling</h3><p>Numerical analysis of ground temperatures.</p></div>
    </div>
    <div class="foot"><div class="logo small"><span class="mark"></span>Tundraline</div><small>Tundraline Permafrost Consulting Ltd. | Confidential</small><div class="pg">5</div></div>
  </section>

  <section class="slide services-slide">
    <div class="banner"><h2>Core Services</h2></div>
    <div class="services">
      <div class="svc"><div class="photo g4" role="img" aria-label="Photo of ground temperature monitoring equipment"></div><h3>Ground Thermal Analysis and Monitoring</h3><p>Instrument install and data review.</p></div>
      <div class="svc"><div class="photo g5" role="img" aria-label="Photo of surface water in thawing tundra"></div><h3>Surface and Groundwater Interactions</h3><p>Water flow effects on frozen ground.</p></div>
      <div class="svc"><div class="photo g6" role="img" aria-label="Aerial photo of northern terrain"></div><h3>Terrain and Hazard Mapping</h3><p>Mapping of landforms and ground risks.</p></div>
    </div>
    <div class="foot"><div class="logo small"><span class="mark"></span>Tundraline</div><small>Tundraline Permafrost Consulting Ltd. | Confidential</small><div class="pg">6</div></div>
  </section>

  <section class="slide services-slide">
    <div class="banner"><h2>Core Services</h2></div>
    <div class="services">
      <div class="svc"><div class="photo g7" role="img" aria-label="Photo of a gravel road on permafrost"></div><h3>Infrastructure Performance Monitoring</h3><p>Tracking settlement and ground movement.</p></div>
      <div class="svc"><div class="photo g8" role="img" aria-label="Photo of a slope affected by thaw"></div><h3>Geohazard Mitigation</h3><p>Design measures for thaw related hazards.</p></div>
      <div class="svc"><div class="photo g9" role="img" aria-label="Photo of engineering documents being reviewed"></div><h3>Third Party Review</h3><p>Independent checks of designs and reports.</p></div>
    </div>
    <div class="foot"><div class="logo small"><span class="mark"></span>Tundraline</div><small>Tundraline Permafrost Consulting Ltd. | Confidential</small><div class="pg">7</div></div>
  </section>

  <section class="slide contact-slide">
    <div class="contact-logo"><div class="logo"><span class="mark"></span>Tundraline</div></div>
    <div class="contact-band">
      <h2>Contact Us</h2>
      <ul class="contact-list">
        <li><svg viewBox="0 0 24 24" fill="#fff"><path d="M6.6 10.8a15 15 0 0 0 6.6 6.6l2.2-2.2a1 1 0 0 1 1-.25 11.4 11.4 0 0 0 3.6.57 1 1 0 0 1 1 1V20a1 1 0 0 1-1 1A17 17 0 0 1 3 4a1 1 0 0 1 1-1h3.5a1 1 0 0 1 1 1c0 1.25.2 2.45.57 3.6a1 1 0 0 1-.25 1z"/></svg>(555) 014-2290</li>
        <li><svg viewBox="0 0 24 24" fill="none" stroke="#fff" stroke-width="2"><rect x="3" y="5" width="18" height="14"/><path d="M3 6l9 7 9-7"/></svg>hello@tundraline-example.com</li>
        <li><svg viewBox="0 0 24 24" fill="none" stroke="#fff" stroke-width="2"><circle cx="12" cy="12" r="9"/><path d="M3 12h18M12 3c3 3 3 15 0 18M12 3c-3 3-3 15 0 18"/></svg>www.tundraline-example.com</li>
      </ul>
    </div>
  </section>

</div>
</body>
</html>
```